winelabels - new design - redesign the existing winelabels

we want to redesign our winelabels, but we want to keep the basic idea of the labels. we want to have a connection to the new label (see sample). Only the basic information should be on the main label, all other informations should be on the side, like in the new label.
restrictions - not wider than 12 cm, the high is fexibel.
we have about 12 different pictures we use for our labels. They have two different highst (see samples). we have two different types of bottles. If you need more information, please give response.
May have a look to our homepage and our shop under www.falkenried-harbacher.de

Reason: there are a lot of very good ideas, but we are still looking for the "perfect" idea

Font styles to use
Other font styles liked:
• for the name "falkenried-harbächer" use the font simelar to the design " Riesling or Muscaris" everthing else is open

Requirements
Must have
• a connection between old an new design

```html
<!DOCTYPE html>
<html lang="de">
<head>
<meta charset="utf-8">
<title>Falkenried-Harbächer Riesling – Etikett</title>
<link rel="stylesheet" href="https://fonts.googleapis.com/css2?family=Reenie+Beanie&family=Libre+Baskerville&display=swap">
<style>
  :root {
    --page: #ffffff;
    --paper: #f4f0e9;
    --paper-shade: #e9e3d9;
    --ink: #4e2c1b;
    --frame: #7a4a32;
    --ornament: #dcae90;
    --shell-light: #d9cbbb;
    --shell-mid: #a88a70;
    --shell-dark: #6b4a33;
    --snail: #c9a677;
  }
  html, body {
    margin: 0;
    width: 1200px;
    height: 1148px;
    overflow: hidden;
    background: var(--page);
  }
  .canvas {
    position: relative;
    width: 1200px;
    height: 1148px;
  }
  .label {
    position: absolute;
    left: 300px;
    top: 74px;
    width: 600px;
    height: 1000px;
  }
  .label-shape {
    position: absolute;
    inset: 0;
    width: 600px;
    height: 1000px;
  }
  .top-ornament {
    position: absolute;
    left: 255px;
    top: 58px;
    width: 90px;
    height: 34px;
    border-radius: 17px;
    background: radial-gradient(ellipse at center, var(--ornament) 0%, rgba(220,174,144,0.25) 75%, transparent 100%);
  }
  .estate-mark {
    position: absolute;
    left: 0;
    right: 0;
    top: 178px;
    text-align: center;
    font-family: "Libre Baskerville", serif;
    font-size: 17px;
    letter-spacing: 1px;
    color: var(--ink);
  }
  .shell-art {
    position: absolute;
    left: 100px;
    top: 250px;
    width: 400px;
    height: 380px;
    border-radius: 50% 50% 42% 42%;
    background: radial-gradient(circle at 48% 45%, var(--shell-light) 0%, var(--shell-mid) 55%, var(--shell-dark) 100%);
    opacity: 0.85;
  }
  .divider {
    position: absolute;
    left: 60px;
    top: 690px;
    width: 480px;
    height: 60px;
  }
  .divider-line {
    position: absolute;
    left: 0;
    right: 0;
    top: 29px;
    border-top: 2px dotted var(--frame);
  }
  .divider-flourish {
    position: absolute;
    top: 18px;
    width: 24px;
    height: 24px;
    border-radius: 50%;
    background: var(--ornament);
    opacity: 0.7;
  }
  .divider-flourish.left { left: 160px; }
  .divider-flourish.right { left: 296px; }
  .snail-photo {
    position: absolute;
    left: 210px;
    top: 0;
    width: 60px;
    height: 60px;
    border-radius: 50%;
    background: radial-gradient(circle at 45% 40%, #efdcbc 0%, var(--snail) 55%, #8f6a44 100%);
  }
  .estate-name {
    position: absolute;
    left: 0;
    right: 0;
    top: 760px;
    text-align: center;
    font-family: "Reenie Beanie", cursive;
    font-size: 66px;
    line-height: 1;
    color: var(--ink);
  }
  .variety {
    position: absolute;
    left: 0;
    right: 0;
    top: 852px;
    text-align: center;
    font-family: "Libre Baskerville", serif;
    font-size: 22px;
    letter-spacing: 1px;
    color: var(--ink);
  }
</style>
</head>
<body>
<main class="canvas">
  <section class="label">
    <svg class="label-shape" viewBox="0 0 600 1000" aria-hidden="true">
      <defs>
        <linearGradient id="paper-tone" x1="0" y1="0" x2="1" y2="1">
          <stop offset="0" stop-color="var(--paper)"/>
          <stop offset="1" stop-color="var(--paper-shade)"/>
        </linearGradient>
      </defs>
      <path fill="url(#paper-tone)" stroke="#d8d0c4" stroke-width="1"
        d="M0,118 L0,110 Q0,96 14,98 L190,100 C240,100 270,70 285,22 L300,0 L315,22 C330,70 360,100 410,100 L586,98 Q600,96 600,110 L600,984 Q600,1000 584,1000 L16,1000 Q0,1000 0,984 Z"/>
      <path fill="none" stroke="var(--frame)" stroke-width="1.5"
        d="M12,124 Q12,112 24,112 L192,112 C246,112 278,82 292,38 L300,24 L308,38 C322,82 354,112 408,112 L576,112 Q588,112 588,124 L588,976 Q588,988 576,988 L24,988 Q12,988 12,976 Z"/>
    </svg>

    <div class="top-ornament" role="img" aria-label="Zierornament in Kupferton"></div>
    <div class="estate-mark">Falkenried-Harbächer</div>
    <div class="shell-art" role="img" aria-label="Sepia-Zeichnung eines Ammoniten"></div>

    <div class="divider">
      <div class="divider-line"></div>
      <div class="divider-flourish left" role="img" aria-label="kleines Zierelement"></div>
      <div class="snail-photo" role="img" aria-label="Foto eines Schneckenhauses"></div>
      <div class="divider-flourish right" role="img" aria-label="kleines Zierelement"></div>
    </div>

    <h1 class="estate-name" style="margin:0;font-weight:400;">Falkenried-Harbächer</h1>
    <p class="variety" style="margin:0;">RIESLING</p>
  </section>
</main>
</body>
</html>
```